Facelift for a tiny Ice Cream and Coffee shop website, etc

Revamp of website to be mobile friendly. It is an Ice Cream and Coffee shop entering a very interesting time of Social Distance and what. I like fun, quirky and offbeat. My theme is 60's, Hawaiian, Surf, just for the fun of it.
also would like a design for business cards, rack cards and to-go menus
Updates

I was hoping to see some really original off beat submissions. Most of the submissions so far look the same as what I have, just rearranged.

I am looking for a design that is "out there", edgy, quirky, unusual, off beat, reflective of our little shop. Outside the box.

Target Market(s)

whomever is Googling "Ice Cream" near me

Contact Information for Business Card

Made on the Farm Ice Cream
from the Milk of Pampered Cows
287 N Harlow Ave
Falls Church, VA 22813
www.OakPorchScoops.com

Number of Pages Required

3 page

Font styles to use
Sans Serif

Colors
6b449b

Requirements
Must have
• Must visit site at OakPorchScoops.com. I want photo with giant pink cone first thing you see. After that I want a pleasing meaningful layout that will get people to visit my shop. The Ice Cream is Made on the farm
Nice to have
• I like my 60's Hawaiian theme, but would be open to Space Age,
Should not have
• Soft serve ice cream

```html
<!DOCTYPE html>
<html lang="en">
<head>
<meta charset="utf-8">
<title>Oak Porch Scoops</title>
<link rel="stylesheet" href="https://fonts.googleapis.com/css2?family=Lobster&family=Poppins:wght@400;500;600;700&display=swap">
<style>
:root{
  --crimson:#a81d3f;
  --footer:#b61b46;
  --teal:#2a8aa3;
  --mint:#b4e8d7;
  --mint-deep:#8dc7b2;
  --ink:#4a4a4a;
  --brown:#6b3b1f;
  --white:#ffffff;
}
*{box-sizing:border-box;margin:0;padding:0}
html,body{width:1200px;height:4082px;overflow:hidden}
body{position:relative;font-family:"Poppins",sans-serif;color:var(--ink);background:var(--white)}
.abs{position:absolute}
.script{font-family:"Lobster",cursive;color:var(--crimson);font-weight:400}

/* hero */
.hero{left:0;top:0;width:1200px;height:700px;background:linear-gradient(180deg,#f8c3c0 0%,#fbe3b5 22%,#fbf0ad 40%,#d9ecc0 70%,#a7dbdd 100%)}
.nav{top:80px;font-size:12.5px;font-weight:600;letter-spacing:.3px;color:#6a4a3a;text-transform:uppercase;display:flex;gap:34px;padding-bottom:12px;border-bottom:1px solid #c9a99a}
.nav.left{left:88px}
.nav.right{left:713px}
.brand{left:520px;top:60px;width:160px;text-align:center;font-family:"Poppins",sans-serif;font-weight:700;font-size:22px;line-height:1.1;color:var(--crimson)}
.brand-dot{display:block;width:40px;height:40px;border-radius:50%;background:var(--crimson);margin:0 auto 8px}
.cart{left:1088px;top:80px}
.welcome{left:88px;top:290px;width:474px;text-align:center;font-size:44px}
.welcome::before,.welcome::after{content:"";position:absolute;top:24px;width:98px;height:6px;border-top:1px solid var(--crimson);border-bottom:1px solid var(--crimson)}
.welcome::before{left:0}.welcome::after{right:0}
.title{left:60px;top:325px;width:530px;text-align:center;font-size:66px;line-height:1}
.btn{display:block;background:var(--teal);color:var(--white);font-weight:600;font-size:14px;text-transform:uppercase;text-align:center;border-radius:26px;box-shadow:0 4px 0 #1d6679}
.hero-btn{left:212px;top:423px;width:224px;height:48px;line-height:48px}
.hero-cone{left:640px;top:160px;width:500px;height:630px;border-radius:45% 45% 40% 40%/40% 40% 60% 60%;background:radial-gradient(circle at 55% 25%,#f6b2d3 0%,#e98ab9 22%,#6b3a22 45%,#e4a656 62%,rgba(228,166,86,0) 75%)}
.clouds{left:0;top:560px}

/* flavors */
.flavors-title{left:0;top:790px;width:1200px;text-align:center;font-size:70px}
.flavor{top:903px;width:210px;text-align:center}
.flavor .scoop{width:158px;height:238px;margin:0 auto;border-radius:79px 79px 40px 40px;}
.flavor h3{margin-top:24px;font-size:16px;font-weight:600;color:var(--brown)}
.flavor p{font-size:13.5px;color:#555;margin-top:4px}
.dots{left:572px;top:1252px;display:flex;gap:8px}
.dots span{width:14px;height:14px;border-radius:50%;border:2px solid #777}
.dots span.on{border-color:#333;box-shadow:inset 0 0 0 2px #fff,inset 0 0 0 6px #333}

/* story */
.story-bg{left:0;top:1280px}
.story-scoops{left:824px;top:1434px;width:318px;height:186px;border-radius:50% 50% 20% 20%;background:linear-gradient(180deg,#c4a0e0 0%,#f2d67a 40%,#e88fb0 65%,#d9a866 100%)}
.story-title{left:645px;top:1660px;font-size:62px;line-height:.78}
.story-copy{left:645px;top:1782px;width:452px;font-size:14px;line-height:1.3;color:#3f4f4c}
.story-copy p{margin-bottom:14px}

/* gallery */
.eyebrow{left:266px;top:2290px;width:200px;text-align:center;font-size:14px;font-weight:600;color:var(--teal);text-transform:uppercase}
.gallery-title{left:150px;top:2305px;width:430px;text-align:center;font-size:62px}
.tile{border-radius:8px}
.tile-overlay{display:flex;align-items:center;justify-content:center;gap:12px;background:rgba(42,130,155,.88)}
.tile-overlay span{width:36px;height:36px;border-radius:50%;background:var(--white);display:flex;align-items:center;justify-content:center}

/* cows */
.cow-title{left:84px;top:2960px;width:560px;font-size:60px;line-height:.78}
.cow-copy{left:84px;top:3100px;width:505px;font-size:14px;line-height:1.6;color:#555}
.cow-btn{left:84px;top:3289px;width:190px;height:48px;line-height:48px}
.cow-img{left:690px;top:2950px;width:420px;height:540px;border-radius:40% 40% 20% 20%;background:linear-gradient(160deg,#f5f5f5 0%,#1d1d1d 35%,#f2f2f2 55%,#222 75%,#e8d7d0 100%)}

/* footer */
.footer-bg{left:0;top:3440px}
.news-title{left:0;top:3545px;width:1200px;text-align:center;font-size:62px;color:var(--white)}
.news-form{left:274px;top:3630px;width:646px;height:52px;border-radius:26px;background:var(--white);display:flex;align-items:center;padding-left:24px;font-size:15px;color:#777}
.news-form svg{margin-right:12px}
.subscribe{position:absolute;right:4px;top:4px;width:162px;height:44px;line-height:44px;font-size:14px;box-shadow:none}
.foot-brand{left:88px;top:3760px;width:180px;text-align:center;font-size:22px;font-weight:700;color:var(--white);line-height:1.15}
.foot-brand .brand-dot{background:var(--white)}
.social{left:94px;top:3904px;display:flex;gap:10px}
.social span{width:35px;height:35px;border-radius:50%;border:2px solid rgba(255,255,255,.55)}
.vline{top:3760px;width:1px;height:230px;background:rgba(255,255,255,.25)}
.foot-col h4{font-family:"Lobster",cursive;font-weight:400;font-size:25px;color:var(--white);margin-bottom:12px}
.foot-col{color:var(--white);font-size:13.5px}
.foot-col li{list-style:none;line-height:24px}
.hours li{display:flex}
.hours li b{font-weight:400;width:72px}
.contact li{display:flex;gap:10px;margin-bottom:18px;line-height:17px}
.contact strong{display:block;font-weight:600;font-size:12.5px}
.rule{left:84px;top:4020px;width:1032px;height:1px;background:rgba(255,255,255,.3)}
.copyright{left:0;top:4042px;width:1200px;text-align:center;font-size:13px;color:var(--white)}
.to-top{left:1124px;top:4000px;width:41px;height:41px;border-radius:50%;background:var(--teal);display:flex;align-items:center;justify-content:center}
</style>
</head>
<body>

<!-- hero -->
<section class="hero abs"></section>
<svg class="clouds abs" width="1200" height="150" viewBox="0 0 1200 150" aria-hidden="true">
  <path fill="#fff" d="M0,95 C15,70 45,65 60,80 C75,50 120,40 145,65 C170,40 215,45 230,75 C250,60 275,70 280,90 L280,150 L0,150 Z"/>
  <path fill="#fff" d="M250,150 L250,110 C280,80 330,90 350,110 C380,70 440,60 470,95 C500,40 560,20 590,60 C620,40 650,60 650,90 L650,150 Z"/>
  <path fill="#fff" d="M960,150 L960,100 C990,70 1030,75 1050,95 C1080,55 1140,55 1160,85 C1180,70 1200,75 1200,80 L1200,150 Z"/>
</svg>

<nav class="nav left abs"><span>Home</span><span>Ice Cream</span><span>Coffee &amp; Espresso</span><span>Smoothies</span></nav>
<nav class="nav right abs"><span>Gift Cards</span><span>Magnets</span><span>Mugs</span><span>T-Shirts</span></nav>
<div class="brand abs"><span class="brand-dot"></span>Oak Porch Scoops</div>
<svg class="cart abs" width="24" height="22" viewBox="0 0 24 22" aria-label="Cart"><path d="M1 2h4l3 12h12l2-8H7" fill="none" stroke="#6a4a3a" stroke-width="1.6"/><circle cx="9" cy="18" r="1.8" fill="#6a4a3a"/><circle cx="19" cy="18" r="1.8" fill="#6a4a3a"/></svg>

<h2 class="welcome abs script">Welcome To</h2>
<h1 class="title abs script">Oak Porch Scoops</h1>
<a class="btn hero-btn abs">Download Menu</a>
<div class="hero-cone abs" role="img" aria-label="Giant pink ice cream cone with chocolate drizzle, sprinkles and candies"></div>

<!-- flavors -->
<h2 class="flavors-title abs script">Flavors</h2>
<div class="flavor abs" style="left:63px"><div class="scoop" role="img" aria-label="Coconut ice cream cone" style="background:linear-gradient(180deg,#cdf7cd 0%,#9ce7a8 40%,#d6a565 100%)"></div><h3>Coconut</h3><p>None better than this</p></div>
<div class="flavor abs" style="left:277px"><div class="scoop" role="img" aria-label="Mango sorbet cone" style="background:linear-gradient(180deg,#fde0df 0%,#f48aa7 40%,#d6a565 100%)"></div><h3>Mango Sorbet</h3><p>Non Dairy and Delicious</p></div>
<div class="flavor abs" style="left:493px"><div class="scoop" role="img" aria-label="Salty caramel cone" style="background:linear-gradient(180deg,#eedcf5 0%,#d48bd6 40%,#d6a565 100%)"></div><h3>Salty Caramel</h3><p>A little Salty and very</p></div>
<div class="flavor abs" style="left:708px"><div class="scoop" role="img" aria-label="Cookies n cream cone" style="background:linear-gradient(180deg,#fdf3b3 0%,#f1e27a 40%,#d6a565 100%)"></div><h3>Cookies n Cream</h3><p>A Crowd Favorite</p></div>
<div class="flavor abs" style="left:924px"><div class="scoop" role="img" aria-label="Chocolate thunder cone" style="background:linear-gradient(180deg,#fde2cb 0%,#7a4a35 40%,#d6a565 100%)"></div><h3>Chocolate Thunder</h3><p>Dense Dark Chocolate</p></div>
<div class="dots abs"><span></span><span class="on"></span><span></span></div>

<!-- story -->
<svg class="story-bg abs" width="1200" height="980" viewBox="0 0 1200 980" aria-hidden="true">
  <path fill="var(--mint-deep)" d="M0,900 C200,940 400,900 600,860 C800,820 1000,790 1200,800 L1200,840 C1000,800 750,890 500,945 C300,985 100,985 0,970 Z"/>
  <path fill="var(--mint)" d="M0,30 C250,-15 500,30 700,190 C850,300 1000,345 1200,335 L1200,830 C1000,790 750,880 500,935 C300,975 100,970 0,955 Z"/>
  <path fill="#d55b69" d="M60,230 C110,160 200,170 230,220 L200,700 C160,760 90,760 50,660 C20,520 20,320 60,230 Z"/>
  <path fill="url(#ice)" role="img" aria-label="Ice cream cones resting on blue crushed ice" d="M0,400 C40,220 220,130 390,170 C520,200 610,320 602,470 C590,620 470,740 320,770 C180,800 60,760 0,700 Z"/>
  <defs><linearGradient id="ice" x1="0" y1="0" x2="1" y2="1"><stop offset="0" stop-color="#6fd3e6"/><stop offset=".55" stop-color="#3fb7d4"/><stop offset="1" stop-color="#8ad9e6"/></linearGradient></defs>
</svg>
<div class="story-scoops abs" role="img" aria-label="Row of colourful ice cream cones"></div>
<h2 class="story-title abs script">Out of this world<br>ice cream</h2>
<div class="story-copy abs">
  <p>We feature Farm Made Ice Cream from Maplebrook Creamery.</p>
  <p>They make Ice Cream from the milk of their Uber-pampered Grass-Fed Jersey Cows. The result is a super smooth, ultra-creamy, but not overly sweet Ice Cream.</p>
  <p>Our shop is very tiny and at the current time there is no indoor seating, but plenty of outside options and a nice canopy in case the weather gets wet.</p>
  <p>To abide by Social Distancing guidelines, we have configured the shop so that there is only enough room inside for one party at a time.</p>
</div>

<!-- gallery -->
<div class="eyebrow abs">Portfolio</div>
<h2 class="gallery-title abs script">Latest Gallery</h2>
<div class="tile abs" role="img" aria-label="Cartoon figurine in yellow shirt" style="left:604px;top:2243px;width:203px;height:198px;background:linear-gradient(160deg,#9db0c8,#e9c778 60%,#c94f3d)"></div>
<div class="tile abs" role="img" aria-label="Three cartoon family figurines on a shelf" style="left:830px;top:2243px;width:202px;height:198px;background:linear-gradient(160deg,#c9d67a,#3d6d8b 55%,#e0a0a8)"></div>
<div class="tile tile-overlay abs" style="left:166px;top:2465px;width:203px;height:198px">
  <span><svg width="16" height="16" viewBox="0 0 16 16" aria-label="Search"><circle cx="7" cy="7" r="4.5" fill="none" stroke="#222" stroke-width="2"/><path d="M10.5 10.5L14 14" stroke="#222" stroke-width="2"/></svg></span>
  <span><svg width="16" height="16" viewBox="0 0 16 16" aria-label="Link"><path d="M6.5 9.5l3-3M5 8l-1.5 1.5a2.5 2.5 0 003.5 3.5L8.5 11.5M11 8l1.5-1.5a2.5 2.5 0 00-3.5-3.5L7.5 4.5" fill="none" stroke="#222" stroke-width="1.6"/></svg></span>
</div>
<div class="tile abs" role="img" aria-label="Group of collectible figurines on display" style="left:385px;top:2460px;width:423px;height:330px;background:linear-gradient(150deg,#8a8f98,#c9825c 40%,#3f5c8a 70%,#b9a24c)"></div>
<div class="tile abs" role="img" aria-label="Cartoon figurine close up" style="left:830px;top:2465px;width:202px;height:198px;background:linear-gradient(160deg,#2a2f5a,#f0d23a 55%,#d9d9d9)"></div>
<div class="tile abs" role="img" aria-label="Cartoon figurine with red telephone" style="left:830px;top:2682px;width:202px;height:195px;background:linear-gradient(160deg,#7a5a6a,#f0b030 50%,#d8324a)"></div>

<!-- cows -->
<h2 class="cow-title abs script">The scret to this ice cream pamered cows</h2>
<p class="cow-copy abs">At Maplebrook Farm Creamery in Millbrook, Delaware, ice Cream is all about Jersey cows. (Jerseys are the brown ones; Holsteins are black and white.) A herd of thirty Jerseys is moved to a fresh field every day after their morning milk-ing, giving them plush green grass to eat and allowing the previous days' fields of clover, alfalfa, orchard, and rye grasses to flourish again. Although a Jersey cow's udders yield significantly less than a Holstein's, the milk's luxurious character makes superior ice cream.</p>
<a class="btn cow-btn abs">Find Out More</a>
<div class="cow-img abs" role="img" aria-label="Black and white dairy cow standing"></div>

<!-- footer -->
<svg class="footer-bg abs" width="1200" height="642" viewBox="0 0 1200 642" aria-hidden="true">
  <path fill="var(--footer)" d="M0,130 C150,60 350,40 520,80 C560,40 700,10 850,25 C1000,40 1120,40 1200,15 L1200,642 L0,642 Z"/>
</svg>
<h2 class="news-title abs">Newsletter</h2>
<div class="news-form abs">
  <svg width="18" height="14" viewBox="0 0 18 14" aria-label="Email"><rect x="1" y="1" width="16" height="12" rx="1.5" fill="#aaa"/><path d="M1 2l8 6 8-6" fill="none" stroke="#fff" stroke-width="1.4"/></svg>
  Enter your email address
  <a class="btn subscribe">Subscribe</a>
</div>

<div class="foot-brand abs"><span class="brand-dot"></span>Oak Porch Scoops</div>
<div class="social abs" aria-label="Social links"><span></span><span></span><span></span><span></span></div>
<div class="vline abs" style="left:322px"></div>
<div class="vline abs" style="left:563px"></div>
<div class="vline abs" style="left:824px"></div>

<div class="foot-col abs" style="left:400px;top:3748px">
  <h4>Quick Links</h4>
  <ul><li>Home</li><li>Ice Cream</li><li>Coffee &amp; Espresso</li><li>Smoothies</li><li>GIFT CARDS</li><li>Magnets</li><li>Mugs</li><li>T Shirts</li></ul>
</div>
<div class="foot-col hours abs" style="left:630px;top:3748px">
  <h4>Opening hours</h4>
  <ul><li><b>Mon</b>Closed</li><li><b>Tues</b>Closed</li><li><b>Wed</b>Closed</li><li><b>Thurs</b>Closed</li><li><b>Fri</b>2 PM - 8 PM</li><li><b>Sat</b>11 AM - 8 PM</li><li><b>Sun</b>11 AM - 6 PM</li></ul>
</div>
<div class="foot-col contact abs" style="left:884px;top:3740px">
  <h4>Contact Info</h4>
  <ul>
    <li><svg width="12" height="12" viewBox="0 0 12 12" aria-label="Phone"><path d="M2 1l2 0 1 3-1.5 1a6 6 0 003.5 3.5L8 7l3 1 0 2c0 1-1 1.5-2 1.5A9 9 0 01.5 3C.5 2 1 1 2 1z" fill="#7fd0e0"/></svg><div><strong>Phone</strong>Text -703 555-0142</div></li>
    <li><svg width="12" height="10" viewBox="0 0 12 10" aria-label="Email"><rect width="12" height="10" rx="1" fill="#7fd0e0"/><path d="M0 1l6 4 6-4" fill="none" stroke="#b61b46"/></svg><div><strong>Email</strong>info@example.com</div></li>
    <li><svg width="10" height="14" viewBox="0 0 10 14" aria-label="Location"><path d="M5 0a5 5 0 015 5c0 4-5 9-5 9S0 9 0 5a5 5 0 015-5z" fill="#7fd0e0"/><circle cx="5" cy="5" r="1.8" fill="#b61b46"/></svg><div><strong>Location</strong>287 N Harlow Ave<br>Falls Church, VA 22813</div></li>
  </ul>
</div>
<div class="rule abs"></div>
<div class="copyright abs">© 2020 by Oak Porch. All Rights Reserved</div>
<div class="to-top abs"><svg width="12" height="8" viewBox="0 0 12 8" aria-label="Back to top"><path d="M1 7l5-5 5 5" fill="none" stroke="#fff" stroke-width="2"/></svg></div>

</body>
</html>
```